Business Card for Voltrix

Horizontal business card for voltrix, the electrical contractor.
clean and professional looking, using company branding and colours.
I also want the blue in the logo and wording to be made a more 'electric' blue and the grey 'Voltrix' to be slightly darker.

Pleas use the following contact details:

Colin Marsh
Owner

t: 01736 582910
m: 07831 206719
e: colin@voltrix-installs.co.uk

www.voltrix-installs.co.uk

Industry/Entity Type

Electrical

Font styles to use
Sans Serif

```html
<!DOCTYPE html>
<html lang="en">
<head>
<meta charset="utf-8">
<title>Voltrix – Business Card</title>
<link rel="stylesheet" href="https://fonts.googleapis.com/css2?family=Nunito:wght@300;400;700;800&display=swap">
<style>
  :root{
    --bg:#e6e4e1;
    --card-black:#0d0d0e;
    --card-charcoal:#2a2a2c;
    --band-grey-light:#a9a7a6;
    --band-grey-dark:#5f5f61;
    --electric-blue:#0a84ff;
    --navy-line:#1f2a8a;
    --brand-grey:#8b8b8e;
    --white:#ffffff;
    --soft-white:#f1f1f1;
  }
  *{box-sizing:border-box;margin:0;padding:0}
  html,body{width:1200px;height:1000px;overflow:hidden}
  body{background:var(--bg);font-family:"Nunito",sans-serif;position:relative}

  .card{
    position:absolute;left:250px;width:700px;height:400px;border-radius:32px;overflow:hidden;
    background:radial-gradient(ellipse at 50% 40%,var(--card-charcoal) 0%,var(--card-black) 75%);
    box-shadow:0 10px 30px rgba(0,0,0,.25);
  }
  .card--front{top:50px}
  .card--back{top:530px}

  /* front */
  .front-brand{position:absolute;left:120px;top:130px;display:flex;align-items:center;gap:22px}
  .front-brand__dot{width:58px;height:58px;border-radius:50%;background:var(--electric-blue)}
  .front-brand__name{font-weight:800;font-size:68px;letter-spacing:10px;color:var(--brand-grey);line-height:1}
  .front-brand__tagline{position:absolute;left:200px;top:212px;font-weight:700;font-size:21px;letter-spacing:4px;color:var(--electric-blue);text-transform:uppercase}
  .front-band{position:absolute;left:0;right:0;bottom:0;height:78px;
    background:linear-gradient(90deg,var(--band-grey-dark),var(--band-grey-light) 60%,var(--band-grey-dark));
    border-top:6px solid var(--electric-blue)}
  .front-band__web{position:absolute;right:40px;top:16px;font-size:30px;font-weight:300;color:var(--soft-white)}

  /* back */
  .back-band{position:absolute;left:0;right:0;bottom:0;height:190px;
    background:linear-gradient(90deg,var(--band-grey-dark),var(--band-grey-light) 55%,var(--band-grey-dark));
    border-top:5px solid var(--navy-line)}
  .back-brand{position:absolute;left:290px;top:62px;color:var(--white)}
  .back-brand__name{font-weight:800;font-size:66px;letter-spacing:2px;line-height:1}
  .back-brand__tagline{font-weight:300;font-size:25px;margin-top:4px}
  .person{position:absolute;left:40px;top:240px;color:var(--white)}
  .person__name{font-weight:800;font-size:32px}
  .person__role{font-weight:300;font-size:30px;color:var(--soft-white)}
  .contacts{position:absolute;right:36px;top:250px;list-style:none;color:var(--white);font-weight:300;font-size:24px;text-align:right}
  .contacts li{display:flex;justify-content:flex-end;align-items:center;gap:12px;line-height:1.4}
  .contacts svg{width:18px;height:18px;fill:none;stroke:var(--soft-white);stroke-width:1.8}
</style>
</head>
<body>

<section class="card card--front" aria-label="Business card front">
  <div class="front-brand">
    <span class="front-brand__dot"></span>
    <span class="front-brand__name">VOLTRIX</span>
  </div>
  <p class="front-brand__tagline">The electrical contractor</p>
  <div class="front-band">
    <span class="front-band__web">www.voltrix-installs.co.uk</span>
  </div>
</section>

<section class="card card--back" aria-label="Business card back">
  <div class="back-brand">
    <div class="back-brand__name">VOLTRIX</div>
    <div class="back-brand__tagline">The electrical contractor</div>
  </div>
  <div class="back-band"></div>
  <div class="person">
    <div class="person__name">Colin Marsh</div>
    <div class="person__role">Owner</div>
  </div>
  <ul class="contacts">
    <li>01736 582910
      <svg viewBox="0 0 24 24" aria-hidden="true"><path d="M5 3h4l2 5-2.5 1.5a11 11 0 0 0 6 6L16 13l5 2v4a2 2 0 0 1-2 2A16 16 0 0 1 3 5a2 2 0 0 1 2-2z"/></svg></li>
    <li>07831 206719
      <svg viewBox="0 0 24 24" aria-hidden="true"><rect x="7" y="2" width="10" height="20" rx="2"/><line x1="11" y1="18" x2="13" y2="18"/></svg></li>
    <li>colin@voltrix-installs.co.uk
      <svg viewBox="0 0 24 24" aria-hidden="true"><rect x="3" y="5" width="18" height="14" rx="1"/><path d="M3 6l9 7 9-7"/></svg></li>
  </ul>
</section>

</body>
</html>
```